Brell Harbor Company Business Cards

Front and Back Business Card - logo and text setup - cool design. I need workable photoshop or illustrator files so I can setup each employee card with design that is created
Updates

Hi everyone, thank you for the great entries. Please no more white and blue cards - there are so many already - black and silver only now please. thanks!

Target Market(s)

Construction Industry - Facility Managers

Industry/Entity Type

Construction

Contact Information for Business Card

I really like contemporary simplistic looks - clean neat....not opposed to seeing some black backrounds

Requirements
Must have
• Logo/website address with design on front only - www.brellharbor-example.com (logo attached)
• Back:
• Name/Title/Company Address/Phone/email address
Nice to have
• Cool design
Should not have
• Nothing gimmicky like Fire or Water - since we are a Fire Protection company - it has all been done

```html
<!DOCTYPE html>
<html lang="en">
<head>
<meta charset="utf-8">
<title>Brell Harbor Company – Business Card</title>
<link rel="stylesheet" href="https://fonts.googleapis.com/css2?family=Nunito+Sans:ital,wght@0,600;0,700;0,800;1,800&display=swap">
<style>
  :root {
    --stage: #e8e8e8;
    --card: #121314;
    --silver: #bfc3c7;
    --silver-bright: #dfe2e5;
    --label: #cfcfcf;
  }
  * { margin: 0; padding: 0; box-sizing: border-box; }
  html, body { width: 1200px; height: 1200px; overflow: hidden; }
  body {
    position: relative;
    background: var(--stage);
    font-family: "Nunito Sans", Arial, sans-serif;
    color: var(--silver);
  }
  .side-label {
    position: absolute;
    left: 66px;
    transform: translate(-50%, -50%) rotate(-90deg);
    font-size: 48px;
    font-weight: 800;
    font-style: italic;
    letter-spacing: 1px;
    color: var(--label);
    white-space: nowrap;
  }
  .side-label--front { top: 284px; }
  .side-label--back { top: 888px; }

  .card {
    position: absolute;
    left: 134px;
    width: 932px;
    height: 533px;
    background: var(--card);
  }
  .card--front { top: 44px; }
  .card--back { top: 622px; }

  .crop-marks { position: absolute; inset: 0; width: 100%; height: 100%; }
  .crop-marks path { fill: none; stroke: var(--silver); stroke-width: 2.4; }

  .brand {
    position: absolute;
    left: 0; right: 0;
    top: 226px;
    text-align: center;
  }
  .brand__name {
    font-size: 60px;
    font-weight: 800;
    line-height: 1;
    color: var(--silver-bright);
  }
  .brand__web {
    margin-top: 22px;
    font-size: 20px;
    font-weight: 700;
    letter-spacing: 1.5px;
    line-height: 1;
    color: var(--silver);
  }

  .card__frame {
    position: absolute;
    top: 36px; left: 35px; right: 35px; bottom: 35px;
    border: 2.4px solid var(--silver);
  }
  .contact {
    position: absolute;
    left: 0; right: 0;
    top: 166px;
    text-align: center;
  }
  .contact__name {
    font-size: 56px;
    font-weight: 800;
    letter-spacing: -0.5px;
    line-height: 1;
    color: var(--silver-bright);
  }
  .contact__title {
    margin-top: 18px;
    font-size: 27px;
    font-weight: 700;
    letter-spacing: 0.5px;
    line-height: 1;
  }
  .contact__details {
    margin-top: 42px;
    font-size: 21px;
    font-weight: 700;
    line-height: 26.6px;
    font-style: normal;
  }
</style>
</head>
<body>
  <span class="side-label side-label--front">COVER</span>
  <span class="side-label side-label--back">BACK</span>

  <section class="card card--front" aria-label="Card front">
    <svg class="crop-marks" viewBox="0 0 932 533" aria-hidden="true">
      <path d="M36 82 V36 H80"/>
      <path d="M852 36 H898 V82"/>
      <path d="M36 450 V498 H80"/>
      <path d="M852 498 H898 V450"/>
    </svg>
    <div class="brand">
      <div class="brand__name">Brell Harbor</div>
      <div class="brand__web">www.brellharbor-example.com</div>
    </div>
  </section>

  <section class="card card--back" aria-label="Card back">
    <div class="card__frame"></div>
    <div class="contact">
      <h1 class="contact__name">Dana Merrow Ellison</h1>
      <p class="contact__title">PRESIDENT</p>
      <address class="contact__details">
        48 Lantern Quay Drive<br>
        Suite C410<br>
        Westmoor, MA 02991<br>
        T: (555) 014-2381, F: (555) 014-2382<br>
        dana@brellharbor-example.com
      </address>
    </div>
  </section>
</body>
</html>
```